Stationary Set Rebrand for Brenton

We are a Canadian Distribution and Service Company that was established in 1969. Over the past 5 decades we have expanded our business and have warehouses across Canada. We specialize in adhesive tapes, adhesives, films, safety, warehouse, shipping, janitorial and packaging supplies.

We have updated our logo design and would like a new corporate branding identity that includes a new fresh Stationary Set (Business Cards, Letterhead, Letterhead MS Word, Envelope, Presentation Folders, Email Signatures, Notepad Covers, etc.)

Target Market(s)

Industrial Business Sector

Font styles to use
Sans Serif

Colors
0054AA
0677BA
7BADD7
CADEEF
E8F1F8
0094D4
00A9DD
6FCCEA
C7EBF8
E9F6FB
00AB8E
00BBA5
67D7C9
C6EFE9
E9F9F6
EB3D1F
EC4F4E
F09395
F8D3D4
FCEDEE

Requirements
Should not have
• Colors not too light, darker colours preferred

```html
<!DOCTYPE html>
<html lang="en">
<head>
<meta charset="utf-8">
<title>Brenton Business Card</title>
<link href="https://fonts.googleapis.com/css2?family=Saira:wght@400;700&family=Michroma&display=swap" rel="stylesheet">
<style>
  :root {
    --page-bg: #dcdcdc;
    --card-white: #ffffff;
    --card-dark: #2f2f2f;
    --ink: #1e1c1c;
    --text-grey: #555555;
    --brand-red: #d81e27;
    --paper-white: #ffffff;
  }
  * { box-sizing: border-box; margin: 0; padding: 0; }
  html, body {
    width: 1200px; height: 1200px; overflow: hidden;
    background: var(--page-bg);
    font-family: "Saira", sans-serif;
  }
  .canvas { position: relative; width: 1200px; height: 1200px; }
  .card {
    position: absolute; left: 252px; width: 696px; height: 398px;
  }
  .card--front { top: 156px; background: var(--card-white); }
  .card--back { top: 651px; background: var(--card-dark); }

  .wordmark {
    position: absolute; display: flex; align-items: center;
    font-family: "Saira", sans-serif; font-weight: 700; line-height: 1;
  }
  .wordmark__name { letter-spacing: -1px; }
  .wordmark__square { background: var(--brand-red); }
  .card--front .wordmark { left: 56px; top: 56px; color: var(--ink); font-size: 64px; gap: 10px; }
  .card--front .wordmark__square { width: 16px; height: 16px; }
  .card--back .wordmark {
    left: 0; right: 0; top: 140px; justify-content: center;
    color: var(--paper-white); font-size: 104px; gap: 14px;
  }
  .card--back .wordmark__square { width: 24px; height: 24px; }

  .address {
    position: absolute; left: 55px; top: 200px;
    color: var(--text-grey); font-size: 17px; line-height: 21px; letter-spacing: 0.5px;
  }
  .contact-list {
    position: absolute; left: 55px; top: 266px; list-style: none;
    color: var(--text-grey); font-size: 17px; letter-spacing: 0.5px;
  }
  .contact-list li { display: flex; align-items: center; height: 21px; }
  .contact-list svg { width: 16px; height: 16px; margin-right: 13px; fill: var(--brand-red); flex: none; }

  .person {
    position: absolute; right: 45px; top: 243px; text-align: right;
  }
  .person__name {
    font-family: "Michroma", sans-serif; color: var(--brand-red);
    font-size: 21px; line-height: 28px; font-weight: 400; letter-spacing: 0.5px;
  }
  .person__title { color: var(--text-grey); font-size: 15px; line-height: 20px; letter-spacing: 0.5px; }
  .accent-bar {
    position: absolute; right: 0; top: 246px; width: 24px; height: 45px;
    background: var(--brand-red);
  }
</style>
</head>
<body>
<main class="canvas">
  <section class="card card--front" aria-label="Business card front">
    <div class="wordmark"><span class="wordmark__name">Brenton</span><span class="wordmark__square"></span></div>

    <p class="address">4120 Harbour Crescent<br>Kingsford, Canada K7L 2R9</p>

    <ul class="contact-list">
      <li><svg viewBox="0 0 16 16" aria-hidden="true"><path d="M3.2 1.2l2.6 2.6-1.5 2a9 9 0 0 0 5.9 5.9l2-1.5 2.6 2.6-1.9 2.1C7.4 14.7 1.3 8.6.9 3.1z"/></svg>613-555-0148</li>
      <li><svg viewBox="0 0 16 16" aria-hidden="true"><path d="M4 0h8a1 1 0 0 1 1 1v14a1 1 0 0 1-1 1H4a1 1 0 0 1-1-1V1a1 1 0 0 1 1-1zm.6 1.6v11h6.8v-11zM8 13.4a.8.8 0 1 0 0 1.6.8.8 0 0 0 0-1.6z"/></svg>613-555-0192</li>
      <li><svg viewBox="0 0 16 16" aria-hidden="true"><path d="M1 3h14v10H1zm1.6 1.6v.3L8 8.7l5.4-3.8v-.3zm0 2.2v4.6h10.8V6.8L8 10.6z"/></svg>info@brenton.com</li>
      <li><svg viewBox="0 0 16 16" aria-hidden="true"><path d="M8 1a7 7 0 1 0 0 14A7 7 0 0 0 8 1zm-1 2.2c.6.5.2 1.4-.5 1.7-.8.3-1.6 1-1.1 1.9.4.7 1.5.4 2 1.1.5.8-.2 1.8.3 2.6.3.5.2 1.4-.3 1.8A5.6 5.6 0 0 1 7 3.2zm3.2.8a5.6 5.6 0 0 1 2.9 6.3c-.6-.6-1.5-.4-2-1.1-.4-.6.3-1.5-.2-2.1-.5-.5-1.5-.3-1.6-1-.1-.9 1.2-1.2.9-2.1z"/></svg>www.brenton.com</li>
    </ul>

    <div class="person">
      <h1 class="person__name">MARK ELLISON</h1>
      <p class="person__title">President</p>
    </div>
    <div class="accent-bar"></div>
  </section>

  <section class="card card--back" aria-label="Business card back">
    <div class="wordmark"><span class="wordmark__name">Brenton</span><span class="wordmark__square"></span></div>
  </section>
</main>
</body>
</html>
```